Designing a website for Brightmoor Pest Services PTY LTD

Pest control company looking for someone to build an informative website containing services we offer and an online inquiry form.
Commercial premises - Specialising in - Rodent control, stored product pest control, flying insect control, ant, spider and insect control, Termite inspections and treatments. Termite management systems on a commercial scale.
Facilities we service
Commercial - shopping centres, transport facilities, restaurants, pubs, clubs, bars food manufacturing facilities.
Residential - Houses specialising in - Rodent, Ant, Spider, Cockroach and Termite control. Termite inspections, Pre - purchase inspections, Termite treatments, Termite management systems.
Target Market(s)
Mainly commercial and industrial clients and Residential clients.
Industry/Entity Type
Pest Control
Number of Pages Required
1 page
Look and feel

```html
<!DOCTYPE html>
<html lang="en">
<head>
<meta charset="utf-8">
<title>Brightmoor Pest Services</title>
<link href="https://fonts.googleapis.com/css2?family=Josefin+Sans:wght@600;700&family=Poppins:wght@400;500;600&display=swap" rel="stylesheet">
<style>
:root{
  --green:#3a8d0f;
  --green-dark:#2f7609;
  --ink:#1d1d1d;
  --muted:#555;
  --sky:#e9f6fb;
  --hero:#efefef;
  --black:#000;
  --footer:#454545;
  --footer-deep:#2d2d2d;
  --white:#fff;
  --star:#f5a300;
}
*{box-sizing:border-box;margin:0;padding:0}
html,body{width:1200px;height:4644px;overflow:hidden}
body{font-family:"Poppins",sans-serif;color:var(--ink);font-size:11px;background:var(--white);position:relative}
h1,h2,h3,h4{font-family:"Josefin Sans",sans-serif}
.wrap{position:absolute;left:159px;width:882px}
section,header{position:absolute;left:0;width:1200px}
.sec-title{text-align:center;font-size:25px;font-weight:700;color:var(--ink)}
.sec-title span{color:var(--green)}
.sec-lead{text-align:center;font-size:10.5px;line-height:19px;color:var(--muted);width:430px;margin:12px auto 0}
.btn{display:inline-block;background:var(--green);color:var(--white);border-radius:20px;font-size:9.5px;font-weight:500;padding:8px 22px}
.btn.dark{background:var(--black)}
.arrow{position:absolute;width:30px;height:30px;display:flex;align-items:center;justify-content:center}
.arrow.black{background:var(--black)}
.arrow.green{background:var(--green)}
/* top bar */
.topbar{top:0;height:29px;background:var(--green);color:var(--white);font-size:9.5px}
.topbar .wrap{top:0;height:29px;display:flex;align-items:center;justify-content:space-between}
.topbar .left{display:flex;gap:18px}
.topbar .left span{display:flex;align-items:center;gap:5px}
/* nav */
.nav{top:29px;height:75px;background:var(--white)}
.nav .wrap{height:75px;display:flex;align-items:center}
.brand{font-family:"Josefin Sans",sans-serif;font-weight:700;font-size:26px;color:var(--ink);display:flex;align-items:center;gap:8px}
.brand i{width:14px;height:14px;background:var(--green);border-radius:50%;display:inline-block}
.menu{display:flex;gap:36px;margin-left:100px;font-size:11px;font-weight:500}
.menu a{color:var(--green);text-decoration:none}
.menu a.on{color:var(--ink)}
.nav .tools{margin-left:auto;display:flex;align-items:center;gap:24px}
/* hero */
.hero{top:104px;height:436px;background:var(--hero)}
.hero h1{position:absolute;left:159px;top:110px;font-size:32px;line-height:38px;color:var(--green);width:520px}
.hero p{position:absolute;left:159px;top:200px;width:430px;font-size:11px;line-height:19px;color:var(--ink)}
.hero .btn{position:absolute;left:159px;top:275px}
.hero .photo{position:absolute;left:700px;top:0;width:500px;height:436px;background:radial-gradient(circle at 45% 55%,#6b6058 0,#b7b0a8 30%,var(--hero) 62%)}
.dots{position:absolute;left:566px;top:375px;display:flex;gap:8px;align-items:center}
.dots i{width:10px;height:10px;border-radius:50%;background:var(--green)}
.dots i.on{width:16px;height:16px;background:transparent;border:2px solid var(--green)}
/* feature band */
.band{top:540px;height:206px;background:var(--black)}
.band .wrap{top:35px;display:flex;gap:18px}
.feat{width:207px;height:137px;background:var(--green);color:var(--white);text-align:center;padding-top:14px;font-size:8.5px;line-height:12px}
.feat .ic{width:38px;height:38px;border:2px solid var(--white);border-radius:50%;margin:0 auto 8px;display:flex;align-items:center;justify-content:center}
.feat h4{font-size:12px;margin-bottom:3px}
.feat .tel{font-size:17px;font-weight:600;margin-top:4px;font-family:"Poppins",sans-serif}
/* our services */
.services{top:746px;height:551px;background:var(--sky)}
.services .sec-title{margin-top:42px}
.svc-row{position:absolute;left:159px;top:204px;display:flex;gap:19px}
.svc{width:281px;height:255px;background:var(--white);text-align:center;position:relative;border-bottom:3px solid var(--green);box-shadow:0 6px 14px rgba(0,0,0,.08);padding-top:68px}
.svc .ic{position:absolute;left:100px;top:-40px;width:80px;height:80px;border-radius:50%;background:var(--green);display:flex;align-items:center;justify-content:center}
.svc h3{font-size:19px;margin-bottom:12px}
.svc p{font-size:10px;line-height:19px;color:var(--muted);padding:0 28px}
.svc hr{border:0;border-top:1px solid #ddd;margin:18px 10px 18px}
.svc.on{background:var(--green);color:var(--white)}
.svc.on p{color:var(--white)}
.svc.on .ic{background:var(--white);border:2px solid var(--green)}
.svc.on hr{border-color:rgba(255,255,255,.5)}
/* why */
.why{top:1297px;height:474px;background:var(--white)}
.why .sec-title{margin-top:42px}
.wbox{position:absolute;width:282px;height:120px;background:var(--white);box-shadow:0 3px 12px rgba(0,0,0,.1);display:flex;gap:14px;padding:30px 14px 0}
.wbox .ic{width:40px;height:40px;border-radius:50%;background:#e6f3df;flex:none;display:flex;align-items:center;justify-content:center}
.wbox .ic.solid{background:var(--green)}
.wbox h4{font-size:14px;margin-bottom:8px}
.wbox p{font-size:9.5px;line-height:18px;color:var(--muted)}
.why .center{position:absolute;left:459px;top:160px;width:282px;text-align:center}
.why .center .logo{height:130px;display:flex;align-items:center;justify-content:center;gap:10px;font-family:"Josefin Sans",sans-serif;font-weight:700;font-size:42px;color:var(--ink)}
.why .center .logo i{width:20px;height:20px;border-radius:50%;background:var(--green)}
.why .center p{font-size:10px;line-height:16px;color:var(--muted);margin:12px 0 14px}
/* process */
.process{top:1771px;height:396px;background:var(--sky)}
.process .sec-title{margin-top:42px;color:var(--green)}
.steps{position:absolute;left:159px;top:160px;width:882px;display:flex;justify-content:space-between}
.step{width:240px;text-align:center}
.step .num{width:66px;height:66px;border-radius:50%;background:var(--green);color:var(--white);font-family:"Josefin Sans",sans-serif;font-size:30px;font-weight:700;margin:0 auto;display:flex;align-items:center;justify-content:center;padding-top:6px;box-shadow:-3px 5px 0 #1b1b1b}
.step h4{color:var(--green);font-size:13.5px;margin:22px 0 8px}
.step p{font-size:9.5px;line-height:16px;color:var(--muted)}
.dash{position:absolute;top:35px}
/* main services */
.main{top:2167px;height:671px;background:var(--white)}
.main .sec-title{margin-top:42px}
.tabs{position:absolute;left:310px;top:161px;width:580px;border-bottom:2px solid #cfe6c4;height:32px;display:flex;justify-content:center;gap:24px;font-size:9px;align-items:flex-start}
.tabs span{padding:5px 14px}
.tabs .on{background:var(--green);color:var(--white);border-radius:14px}
.grid{position:absolute;left:159px;top:224px;display:grid;grid-template-columns:repeat(3,281px);column-gap:19px;row-gap:22px}
.mcard{height:192px;border-radius:80px;background:var(--sky);text-align:center;padding-top:14px}
.mcard .ic{width:52px;height:52px;border-radius:50%;border:2px solid var(--green);background:var(--white);margin:0 auto 12px;display:flex;align-items:center;justify-content:center}
.mcard h4{font-size:14px;margin-bottom:6px}
.mcard p{font-size:9.5px;line-height:15px;color:var(--muted);padding:0 28px}
.mcard a{display:block;margin-top:8px;color:var(--green);font-weight:600;font-size:10px}
.mcard.on{background:var(--green);color:var(--white)}
.mcard.on p,.mcard.on a{color:var(--white)}
/* estimate */
.estimate{top:2838px;height:648px;background:var(--white)}
.estimate .photo{position:absolute;left:115px;top:20px;width:545px;height:628px;background:linear-gradient(180deg,#d9dbdd,#a5a8ac 55%,#5a5d60)}
.form{position:absolute;left:684px;top:56px;width:357px;height:562px;background:var(--white);box-shadow:0 3px 14px rgba(0,0,0,.12);padding:28px 22px}
.form h2{color:var(--green);font-size:23px}
.form .intro{font-size:10px;line-height:18px;color:var(--muted);margin:6px 0 14px}
.form label{display:block;font-size:10.5px;font-weight:500;margin-bottom:8px}
.field{height:30px;border:1px solid #ddd;border-radius:15px;font-size:8.5px;color:#888;padding:9px 16px;margin-bottom:20px;display:flex;justify-content:space-between}
.field.area{height:86px;border-radius:10px}
.form .btn{display:block;width:134px;margin:0 auto;text-align:center}
/* testimonials */
.testi{top:3486px;height:487px;background:var(--white)}
.testi .sec-title{margin-top:42px}
.trow{position:absolute;left:159px;top:145px;display:flex;gap:19px}
.tcard{width:281px;height:238px;background:var(--sky);text-align:center;padding-top:14px}
.tcard .av{width:52px;height:52px;border-radius:50%;background:linear-gradient(#d6d6d6,#b3a79c);margin:0 auto 10px}
.tcard h4{font-size:14px}
.tcard .role{color:var(--green);font-size:9px;margin:3px 0 8px}
.tcard p{font-size:9.5px;line-height:16px;color:var(--muted);padding:0 18px}
.stars{color:var(--star);font-size:12px;letter-spacing:3px;margin:6px 0 2px}
.quote{font-family:"Josefin Sans",sans-serif;font-size:34px;font-weight:700;color:#555;line-height:30px}
/* call */
.call{top:3973px;height:270px;background:var(--sky)}
.callbox{position:absolute;left:159px;top:43px;width:882px;height:173px;background:var(--white);box-shadow:0 3px 12px rgba(0,0,0,.08)}
.callbox .photo{position:absolute;left:0;top:0;width:282px;height:173px;background:linear-gradient(135deg,#2d3945,#6b7a86 55%,#b4bcc1)}
.callbox .phone{position:absolute;left:248px;top:52px;width:68px;height:68px;border-radius:50%;background:var(--green);border:4px solid var(--white);display:flex;align-items:center;justify-content:center}
.callbox h3{position:absolute;left:335px;top:40px;font-size:23px;line-height:33px;font-weight:600}
.callbox h3 span{color:var(--green)}
.callbox p{position:absolute;left:338px;top:112px;width:520px;font-size:10px;line-height:19px;color:var(--muted)}
/* footer */
.footer{top:4243px;height:342px;background:var(--footer);color:#eee}
.fbrand{position:absolute;left:171px;top:52px;font-family:"Josefin Sans",sans-serif;font-weight:700;font-size:30px;color:var(--white);display:flex;align-items:center;gap:8px}
.fbrand i{width:16px;height:16px;border-radius:50%;background:var(--green)}
.fabout{position:absolute;left:171px;top:126px;width:265px;font-size:9.5px;line-height:18px}
.cards{position:absolute;left:171px;top:212px;display:flex;gap:4px}
.cards i{width:38px;height:22px;background:var(--white);border-radius:2px;display:block}
.fcol{position:absolute;top:62px;font-size:9.5px;line-height:21px}
.fcol h4{font-size:13px;color:var(--white);margin-bottom:12px}
.fcol .ci{display:flex;gap:8px;align-items:flex-start}
.social{display:flex;gap:9px;margin-top:8px}
.social i{width:26px;height:26px;border-radius:50%;background:var(--green);display:block}
.news{position:absolute;left:0;width:1200px;top:266px;text-align:center;font-size:10px;font-weight:500;letter-spacing:.3px}
.news .box{margin:9px auto 0;width:282px;height:32px;border-radius:16px;background:var(--white);display:flex;align-items:center;justify-content:space-between;padding-left:18px;color:#777;font-size:8.5px}
.news .box span{background:var(--green);color:var(--white);height:32px;border-radius:16px;padding:0 18px;display:flex;align-items:center;font-size:9.5px;font-weight:600}
.copy{top:4585px;height:59px;background:var(--footer-deep);color:#ddd;font-size:10px;display:flex;align-items:center;justify-content:center}
</style>
</head>
<body>

<header class="topbar">
  <div class="wrap">
    <div class="left">
      <span><svg width="11" height="9" viewBox="0 0 11 9"><rect x=".5" y=".5" width="10" height="8" fill="none" stroke="#fff"/><path d="M.5 .5l5 4 5-4" fill="none" stroke="#fff"/></svg>info@example.com</span>
      <span><svg width="10" height="10" viewBox="0 0 24 24"><path d="M6 2l4 5-2 3c1 3 3 5 6 6l3-2 5 4-3 4C10 21 3 14 2 5z" fill="#fff"/></svg>+123 456-7890</span>
      <span><svg width="9" height="11" viewBox="0 0 12 16"><path d="M6 0a6 6 0 0 0-6 6c0 4 6 10 6 10s6-6 6-10a6 6 0 0 0-6-6z" fill="#fff"/></svg>1st Floor USA</span>
    </div>
    <div>Voluptate velit esse cillum dolore eu fugiat nulla pariatur.</div>
  </div>
</header>

<header class="nav">
  <div class="wrap">
    <div class="brand"><i></i>Brightmoor</div>
    <nav class="menu">
      <a class="on">Home</a><a>About Us</a><a>Our Services ▾</a><a>News</a><a>Contact Us</a>
    </nav>
    <div class="tools">
      <svg width="18" height="18" viewBox="0 0 20 20"><circle cx="8" cy="8" r="6.5" fill="none" stroke="#333" stroke-width="1.6"/><path d="M13 13l6 6" stroke="#333" stroke-width="1.6"/></svg>
      <span class="btn">Get Appointment</span>
    </div>
  </div>
</header>

<section class="hero">
  <div class="photo" role="img" aria-label="Close-up of a fly held between a person's fingers"></div>
  <h1>Termite Treatment, Pest Control &amp; Exterminator Service</h1>
  <p>Lorem ipsum dolor sit amet, consectetur adipiscing elit, sed do eiusmod tempor incididunt ut labore et dolore magna aliqua. Quis ipsum suspendisse ultrices gravida.</p>
  <span class="btn">Get Appointment</span>
  <div class="arrow black" style="left:28px;top:202px"><svg width="10" height="14"><path d="M8 1L2 7l6 6" fill="none" stroke="#fff" stroke-width="1.6"/></svg></div>
  <div class="arrow green" style="left:1137px;top:202px"><svg width="10" height="14"><path d="M2 1l6 6-6 6" fill="none" stroke="#fff" stroke-width="1.6"/></svg></div>
  <div class="dots"><i></i><i class="on"></i><i></i></div>
</section>

<section class="band">
  <div class="wrap">
    <div class="feat"><div class="ic" style="border:0"><svg width="34" height="34" viewBox="0 0 24 24"><path d="M6 2l4 5-2 3c1 3 3 5 6 6l3-2 5 4-3 4C10 21 3 14 2 5z" fill="none" stroke="#fff" stroke-width="1.3"/></svg></div>HOTLINE<h4 style="margin-top:3px">Contact Us Today</h4><div class="tel">+123-456-7890</div></div>
    <div class="feat"><div class="ic"><svg width="16" height="16"><circle cx="8" cy="8" r="5" fill="none" stroke="#fff"/></svg></div><h4>Expert Pest Control</h4>Lorem ipsum dolor sit amet,<br>consectetur adipiscing elit, sed do<br>eiusmod tempor aliqua.</div>
    <div class="feat"><div class="ic"><svg width="16" height="16"><path d="M3 9l3 3 7-8" fill="none" stroke="#fff" stroke-width="1.5"/></svg></div><h4>Satisfaction</h4>Lorem ipsum dolor sit amet,<br>consectetur adipiscing elit, sed do<br>eiusmod tempor aliqua.</div>
    <div class="feat"><div class="ic"><svg width="16" height="16"><circle cx="8" cy="8" r="5" fill="none" stroke="#fff"/><path d="M8 5v3h3" stroke="#fff" fill="none"/></svg></div><h4>24/7 Support</h4>Lorem ipsum dolor sit amet,<br>consectetur adipiscing elit, sed do<br>eiusmod tempor aliqua.</div>
  </div>
</section>

<section class="services">
  <h2 class="sec-title">Our <span>Services</span></h2>
  <p class="sec-lead">Lorem ipsum dolor sit amet, consectetur adipiscing elit. Etiam porttitor orci felis, sit amet rutrum nisi finibus sed.</p>
  <div class="arrow black" style="left:110px;top:314px"><svg width="10" height="14"><path d="M8 1L2 7l6 6" fill="none" stroke="#fff" stroke-width="1.6"/></svg></div>
  <div class="arrow green" style="left:1060px;top:314px"><svg width="10" height="14"><path d="M2 1l6 6-6 6" fill="none" stroke="#fff" stroke-width="1.6"/></svg></div>
  <div class="svc-row">
    <div class="svc"><div class="ic"><svg width="36" height="36" viewBox="0 0 24 24" fill="none" stroke="#fff" stroke-width="1.2"><ellipse cx="12" cy="14" rx="5" ry="7"/><circle cx="12" cy="6" r="2.5"/><path d="M7 11H3M7 15H3M17 11h4M17 15h4M7 19l-3 2M17 19l3 2M10 4L8 1M14 4l2-3"/></svg></div><h3>Service 01</h3><p>Lorem ipsum dolor sit amet, consectetur adipiscing elit. Etiam porttitor orci felis, sit amet rutrum nisi finibus sed.</p><hr><span class="btn">Read More..</span></div>
    <div class="svc on"><div class="ic"><svg width="36" height="36" viewBox="0 0 24 24" fill="none" stroke="#3a8d0f" stroke-width="1.2"><ellipse cx="12" cy="14" rx="5" ry="7"/><circle cx="12" cy="6" r="2.5"/><path d="M7 11H3M7 15H3M17 11h4M17 15h4M7 19l-3 2M17 19l3 2M10 4L8 1M14 4l2-3"/></svg></div><h3>Service 02</h3><p>Lorem ipsum dolor sit amet, consectetur adipiscing elit. Etiam porttitor orci felis, sit amet rutrum nisi finibus sed.</p><hr><span class="btn dark">Read More..</span></div>
    <div class="svc"><div class="ic"><svg width="36" height="36" viewBox="0 0 24 24" fill="none" stroke="#fff" stroke-width="1.2"><ellipse cx="12" cy="14" rx="5" ry="7"/><circle cx="12" cy="6" r="2.5"/><path d="M7 11H3M7 15H3M17 11h4M17 15h4M7 19l-3 2M17 19l3 2M10 4L8 1M14 4l2-3"/></svg></div><h3>Service 03</h3><p>Lorem ipsum dolor sit amet, consectetur adipiscing elit. Etiam porttitor orci felis, sit amet rutrum nisi finibus sed.</p><hr><span class="btn">Read More..</span></div>
  </div>
</section>

<section class="why">
  <h2 class="sec-title">Why <span>Choose</span> Us</h2>
  <p class="sec-lead">Lorem ipsum dolor sit amet, consectetur adipiscing elit. Etiam porttitor orci felis, sit amet rutrum nisi finibus sed.</p>
  <div class="wbox" style="left:159px;top:163px"><div class="ic"><svg width="18" height="18"><rect x="4" y="2" width="10" height="14" fill="none" stroke="#3a8d0f"/></svg></div><div><h4>Top Rated Services</h4><p>Lorem ipsum dolor sit amet, consec tetur adipiscing elit.</p></div></div>
  <div class="wbox" style="left:159px;top:299px"><div class="ic"><svg width="20" height="14"><rect x="1" y="3" width="13" height="8" fill="none" stroke="#3a8d0f"/><path d="M14 6h4l1 5h-5" fill="none" stroke="#3a8d0f"/></svg></div><div><h4>Residential Services</h4><p>Lorem ipsum dolor sit amet, consec tetur adipiscing elit.</p></div></div>
  <div class="wbox" style="left:759px;top:163px"><div class="ic solid"><svg width="18" height="18"><rect x="3" y="5" width="12" height="10" fill="none" stroke="#fff"/></svg></div><div><h4>Commercial Services</h4><p>Lorem ipsum dolor sit amet, consec tetur adipiscing elit.</p></div></div>
  <div class="wbox" style="left:759px;top:299px"><div class="ic"><svg width="18" height="18"><rect x="4" y="2" width="10" height="14" fill="none" stroke="#3a8d0f"/></svg></div><div><h4>Fully Equipmented</h4><p>Lorem ipsum dolor sit amet, consec tetur adipiscing elit.</p></div></div>
  <div class="center">
    <div class="logo"><i></i>Brightmoor</div>
    <p>Lorem ipsum dolor sit amet, consectetur adipiscing elit. Etiam porttitor orci felis, sit amet rutrum nisi finibus sed.</p>
    <span class="btn">Read More..</span>
  </div>
</section>

<section class="process">
  <h2 class="sec-title">Work Process</h2>
  <p class="sec-lead">Lorem ipsum dolor sit amet, consectetur adipiscing elit. Etiam porttitor orci felis, sit amet rutrum nisi finibus sed.</p>
  <div class="steps">
    <svg class="dash" style="left:268px" width="46" height="8"><path d="M0 4h40" stroke="#888" stroke-dasharray="3 3"/><path d="M40 1l4 3-4 3" fill="none" stroke="#888"/></svg>
    <svg class="dash" style="left:568px" width="46" height="8"><path d="M0 4h40" stroke="#888" stroke-dasharray="3 3"/><path d="M40 1l4 3-4 3" fill="none" stroke="#888"/></svg>
    <div class="step"><div class="num">1</div><h4>Online Booking</h4><p>Lorem ipsum dolor sit amet, consectetur adipiscing elit. Etiam porttitor orci felis, sit amet rutrum nisi finibus sed.</p></div>
    <div class="step"><div class="num">2</div><h4>Take Pest Control Advice</h4><p>Lorem ipsum dolor sit amet, consectetur adipiscing elit. Etiam porttitor orci felis, sit amet rutrum nisi finibus sed.</p></div>
    <div class="step"><div class="num">3</div><h4>Apply Pest Control Service</h4><p>Lorem ipsum dolor sit amet, consectetur adipiscing elit. Etiam porttitor orci felis, sit amet rutrum nisi finibus sed.</p></div>
  </div>
</section>

<section class="main">
  <h2 class="sec-title">Our Main <span>Services</span></h2>
  <p class="sec-lead">Lorem ipsum dolor sit amet, consectetur adipiscing elit. Etiam porttitor orci felis, sit amet rutrum nisi finibus sed.</p>
  <div class="tabs"><span>All</span><span class="on">Commercial Services</span><span>Residential Services</span><span>Common Pest Control</span></div>
  <div class="grid">
    <div class="mcard"><div class="ic"><svg width="20" height="20"><rect x="5" y="3" width="10" height="14" fill="none" stroke="#3a8d0f"/></svg></div><h4>Rodent control</h4><p>Lorem ipsum dolor sit amet, consectetur adipiscing elit. Etiam porttitor orci felis, sit amet rutrum nisi finibus sed.</p><a>View Detail</a></div>
    <div class="mcard on"><div class="ic" style="border-color:#fff"><svg width="20" height="20"><rect x="5" y="3" width="10" height="14" fill="none" stroke="#3a8d0f"/></svg></div><h4>Flying insect control</h4><p>Lorem ipsum dolor sit amet, consectetur adipiscing elit. Etiam porttitor orci felis, sit amet rutrum nisi finibus sed.</p><a>View Detail</a></div>
    <div class="mcard"><div class="ic"><svg width="20" height="20"><rect x="5" y="3" width="10" height="14" fill="none" stroke="#3a8d0f"/></svg></div><h4>Ant Control</h4><p>Lorem ipsum dolor sit amet, consectetur adipiscing elit. Etiam porttitor orci felis, sit amet rutrum nisi finibus sed.</p><a>View Detail</a></div>
    <div class="mcard"><div class="ic"><svg width="20" height="20"><rect x="5" y="3" width="10" height="14" fill="none" stroke="#3a8d0f"/></svg></div><h4>Spider &amp; Insect Control</h4><p>Lorem ipsum dolor sit amet, consectetur adipiscing elit. Etiam porttitor orci felis, sit amet rutrum nisi finibus sed.</p><a>View Detail</a></div>
    <div class="mcard"><div class="ic"><svg width="20" height="20"><rect x="5" y="3" width="10" height="14" fill="none" stroke="#3a8d0f"/></svg></div><h4>Termite inspections</h4><p>Lorem ipsum dolor sit amet, consectetur adipiscing elit. Etiam porttitor orci felis, sit amet rutrum nisi finibus sed.</p><a>View Detail</a></div>
    <div class="mcard"><div class="ic"><svg width="20" height="20"><rect x="5" y="3" width="10" height="14" fill="none" stroke="#3a8d0f"/></svg></div><h4>Termite management</h4><p>Lorem ipsum dolor sit amet, consectetur adipiscing elit. Etiam porttitor orci felis, sit amet rutrum nisi finibus sed.</p><a>View Detail</a></div>
  </div>
</section>

<section class="estimate">
  <div class="photo" role="img" aria-label="Technician in a protective suit and respirator holding a fogging sprayer"></div>
  <div class="form">
    <h2>Get a Free Estimate</h2>
    <p class="intro">Lorem ipsum dolor sit amet, consectetur adipiscing elit. Etiam porttitor orci felis, sit amet rutrum nisi finibus sed.</p>
    <label>Full Name</label><div class="field">Enter Your Full Name</div>
    <label>E-Mail</label><div class="field">Enter Your E-Mail</div>
    <label>Phone</label><div class="field">Enter Your Phone Number</div>
    <label>Select Service</label><div class="field">Type of service <span>⌄</span></div>
    <label>Message</label><div class="field area">Write Here..</div>
    <span class="btn">Appointment Now!</span>
  </div>
</section>

<section class="testi">
  <h2 class="sec-title">What Our <span>Client</span> Says</h2>
  <p class="sec-lead">Lorem ipsum dolor sit amet, consectetur adipiscing elit. Etiam porttitor orci felis, sit amet rutrum nisi finibus sed.</p>
  <div class="trow">
    <div class="tcard"><div class="av" role="img" aria-label="Client portrait"></div><h4>John Doe</h4><div class="role">CEO, COMPANY NAME</div><p>Lorem ipsum dolor amet consectet adipiscing sed do eiusmod tempor incididunt labore et dolore magna aliqua ipsum.</p><div class="stars">★★★★★</div><div class="quote">"</div></div>
    <div class="tcard"><div class="av" role="img" aria-label="Client portrait"></div><h4>John Doe</h4><div class="role">CEO, COMPANY NAME</div><p>Lorem ipsum dolor amet consectet adipiscing sed do eiusmod tempor incididunt labore et dolore magna aliqua ipsum.</p><div class="stars">★★★★★</div><div class="quote">"</div></div>
    <div class="tcard"><div class="av" role="img" aria-label="Client portrait"></div><h4>John Doe</h4><div class="role">CEO, COMPANY NAME</div><p>Lorem ipsum dolor amet consectet adipiscing sed do eiusmod tempor incididunt labore et dolore magna aliqua ipsum.</p><div class="stars">★★★★★</div><div class="quote">"</div></div>
  </div>
  <div class="arrow black" style="left:563px;top:407px"><svg width="10" height="14"><path d="M8 1L2 7l6 6" fill="none" stroke="#fff" stroke-width="1.6"/></svg></div>
  <div class="arrow green" style="left:607px;top:407px"><svg width="10" height="14"><path d="M2 1l6 6-6 6" fill="none" stroke="#fff" stroke-width="1.6"/></svg></div>
</section>

<section class="call">
  <div class="callbox">
    <div class="photo" role="img" aria-label="Technicians in protective suits spraying in a garage"></div>
    <div class="phone"><svg width="28" height="28" viewBox="0 0 24 24"><path d="M6 2l4 5-2 3c1 3 3 5 6 6l3-2 5 4-3 4C10 21 3 14 2 5z" fill="none" stroke="#fff" stroke-width="1.4"/></svg></div>
    <h3>Need Our Help or Have Questions?<br>Call Us <span>+1 (123) 456 7890</span></h3>
    <p>Lorem ipsum dolor sit amet, consectetur adipiscing elit. Etiam porttitor orci felis, sit amet rutrum nisi finibus sed.</p>
  </div>
</section>

<footer class="footer" style="position:absolute;left:0;width:1200px">
  <div class="fbrand"><i></i>Brightmoor</div>
  <p class="fabout">Adipiscing elit, sed do eiusmod tempor incididunt ut labore et dolore magna aliqua. Ut enim ad minim veniam, quis nostrud exercitation ullamco laboris.</p>
  <div class="cards"><i></i><i></i><i></i><i></i></div>
  <div class="fcol" style="left:472px"><h4>Our Services</h4>Commercial Pest Control<br>Residential Pest Control<br>Commont Pest Control<br>Our Blog<br>Contact Us</div>
  <div class="fcol" style="left:697px"><h4>Useful Links</h4>About Company<br>Services<br>How It Works<br>Our Blog<br>Contact Us</div>
  <div class="fcol" style="left:847px;width:190px;line-height:16px"><h4>Contact Us</h4>
    <div class="ci" style="margin-bottom:6px">✉ <span>info@example.com</span></div>
    <div class="ci" style="margin-bottom:6px">☏ <span>+123 456-7890</span></div>
    <div class="ci" style="margin-bottom:6px">⌖ <span>Adipiscing elit, sed do eiusmod tempor incididunt ut labore dolore magna.</span></div>
    <div class="ci">◷ <span>Mon-Fri, 7:00am to 9:00pm</span></div>
    <div class="social"><i></i><i></i><i></i><i></i></div>
  </div>
  <div class="news">SUBSCRIBE OUR NEWSLETTER<div class="box">Enter Your E-Mail<span>Subscribe Now</span></div></div>
</footer>

<section class="copy">Copyright 2021 Brightmoor Pest Services All Rights Reserved.</section>

</body>
</html>
```